Brightmere Realty information card

We need a 5x7 two-sided card to hand out at open houses and provide to our charitable partners for distribution. We are a local real estate group looking to add a "give back" component to our business. We are located in a coastal community and would like to incorporate that feel into our design. We are giving clients who use us the ability to designate 1 out of the 10 charitable organizations we partner with - and we will make a donation to that organization.

We included the 10 partner logos below - we envision them pretty small. Also included 2 photos of the "Brightmere" and our logo. Have fun.
Updates

Project Deadline Extended
Reason: We're out of town until Wednesday, May 17th.

Target Market(s)

home buyers & sellers

Industry/Entity Type

Real Estate

Font styles to use
Serif
Sans Serif

Colors

Designer to choose colors to be used in the design.

Requirements
Must have
• slogan & tagline - see attached text file
• Brightmere photo
Nice to have
• partner logos - small - maybe in circles?

```html
<!DOCTYPE html>
<html lang="en">
<head>
<meta charset="utf-8">
<title>Brightmere Realty – Information Card</title>
<link href="https://fonts.googleapis.com/css2?family=Open+Sans:ital,wght@0,400;0,600;0,700;1,600;1,800&display=swap" rel="stylesheet">
<style>
  :root {
    --page: #ffffff;
    --navy: #0d3f96;
    --royal: #0a4fc6;
    --deep: #0b2f86;
    --sky: #5b93e6;
    --ink: #111418;
    --white: #ffffff;
  }
  * { margin: 0; padding: 0; box-sizing: border-box; }
  html, body { width: 927px; height: 1200px; overflow: hidden; background: var(--page); }
  body { position: relative; font-family: "Open Sans", Arial, sans-serif; color: var(--ink); }

  .card { position: absolute; left: 82px; width: 763px; height: 545px; overflow: hidden; }
  .card--front { top: 36px; }
  .card--back { top: 618px; }

  /* Front */
  .coast-photo {
    position: absolute; inset: 0;
    background:
      radial-gradient(ellipse 260px 60px at 300px 320px, rgba(240,170,165,0.75), rgba(240,170,165,0) 100%),
      radial-gradient(ellipse 420px 150px at 80px 150px, rgba(250,200,120,0.55), rgba(250,200,120,0) 100%),
      linear-gradient(180deg,
        #c98a9a 0%, #e49a86 14%, #f0a67e 26%, #f2b58c 36%,
        #d9a0a4 46%, #c99aa8 52%, #b48aa0 58%, #6a5468 64%,
        #4c4456 70%, #3c3a4c 78%, #34303e 88%, #2a2630 100%);
  }
  .front-swoosh { position: absolute; inset: 0; width: 763px; height: 545px; }

  .brand {
    position: absolute; left: 22px; top: 70px; width: 200px;
    text-align: center; color: var(--white);
    font-weight: 600; line-height: 1.1;
  }
  .brand__name { font-size: 36px; display: block; }
  .brand__sub { font-size: 28px; display: block; }

  .slogan {
    position: absolute; right: 12px; top: 128px; white-space: nowrap;
    font-size: 35px; font-weight: 800; font-style: italic;
    color: var(--navy);
    text-shadow: 0 0 2px #fff, 1px 1px 0 #fff, -1px -1px 0 #fff, 1px -1px 0 #fff, -1px 1px 0 #fff;
  }
  .tagline {
    position: absolute; right: 14px; top: 184px; white-space: nowrap;
    font-size: 23px; font-weight: 800; font-style: italic;
    color: #0c0c14;
    text-shadow: 0 0 2px #fff, 1px 1px 0 #fff, -1px -1px 0 #fff, 1px -1px 0 #fff, -1px 1px 0 #fff;
  }
  .front-intro {
    position: absolute; left: 393px; top: 226px; width: 348px;
    font-size: 16px; font-weight: 600; font-style: italic; line-height: 20px;
    text-align: justify; color: #15151c;
  }

  /* Back */
  .sky-photo {
    position: absolute; left: 0; top: 0; width: 763px; height: 278px;
    background: linear-gradient(180deg, #5a90e4 0%, #8fb4ec 45%, #a9c6f0 70%, #7fa8ea 100%);
  }
  .give-title {
    position: absolute; left: 0; right: 0; top: 15px; text-align: center;
    font-size: 26.5px; font-weight: 800; font-style: italic; color: var(--navy);
    text-shadow: 1px 1px 0 #fff, -1px -1px 0 #fff, 1px -1px 0 #fff, -1px 1px 0 #fff;
  }
  .give-list {
    position: absolute; left: 31px; top: 60px; width: 703px;
    list-style: none; font-size: 15.9px; font-weight: 600; line-height: 25.6px;
  }
  .give-list li { text-align: justify; text-align-last: left; }

  .partners {
    position: absolute; left: 0; top: 278px; width: 763px; height: 92px;
    background: var(--royal);
    display: flex; justify-content: space-between; align-items: center;
    padding: 0 16px 0 14px;
  }
  .partner { width: 62px; height: 62px; border-radius: 50%; background: var(--white); border: 2px solid #d9e4f7; }
  .partner--dark { background: #2c2c33; }
  .partner--pink { background: #e79bd0; }

  .town-photo {
    position: absolute; left: 0; top: 370px; width: 763px; height: 175px;
    background: linear-gradient(180deg, #4f7fd6 0%, #5d8ad8 40%, #7ea0d8 100%);
  }
  .back-swoosh { position: absolute; left: 0; top: 370px; width: 763px; height: 175px; }
  .site {
    position: absolute; left: 0; right: 0; top: 390px; text-align: center;
    font-size: 21px; font-weight: 700; letter-spacing: 5.2px; color: var(--white);
  }
  .contacts {
    position: absolute; left: 44px; top: 438px;
    font-size: 18px; line-height: 26px; color: #14161c; list-style: none;
  }
</style>
</head>
<body>

<section class="card card--front">
  <div class="coast-photo" role="img" aria-label="Sunset over the coastal town, with the curving bay, pier and hillside homes"></div>
  <svg class="front-swoosh" viewBox="0 0 763 545" aria-hidden="true">
    <defs>
      <linearGradient id="bandBlue" x1="0" y1="0" x2="1" y2="0">
        <stop offset="0" stop-color="#2f6fd8"/>
        <stop offset="1" stop-color="#0f3d9c"/>
      </linearGradient>
    </defs>
    <path d="M0 0 H763 V108 C640 90 520 60 380 34 C250 12 120 18 0 42 Z" fill="url(#bandBlue)"/>
    <path d="M0 42 C120 18 250 12 380 34 C520 60 640 90 763 108" fill="none" stroke="#fff" stroke-width="5"/>
  </svg>

  <div class="brand">
    <span class="brand__name">Brightmere</span>
    <span class="brand__sub">Realty</span>
  </div>

  <h1 class="slogan">Change Homes, Change Lives</h1>
  <h2 class="tagline">Changing the World One Home at a Time</h2>
  <p class="front-intro">Because we value generosity and desire to make a difference in our community and world, for every home bought or sold through us, we will make a contribution to one of our amazing partner who are helping to change the world.</p>
</section>

<section class="card card--back">
  <div class="sky-photo" role="img" aria-label="Soft blue sky with clouds"></div>
  <h2 class="give-title">We live here.&nbsp; We give here.</h2>
  <ul class="give-list">
    <li>We give because we value generosity and believe we have been blessed to be a blessing.</li>
    <li>We believe that together we can change the world one home at time.</li>
    <li>You have our guarantee of personal service and no additional costs.</li>
    <li>The donations come out of our commission, not your pocket.</li>
    <li>You get to designate which of our amazing partner organizations you would like us to contribute to on behalf of your transaction.</li>
    <li>When you are ready to buy or sell, please consider giving us a call.</li>
    <li>Tell a friend about us too.&nbsp; Together, we can make the world a better place.</li>
  </ul>

  <div class="partners" aria-label="Partner organizations">
    <span class="partner"></span>
    <span class="partner"></span>
    <span class="partner partner--dark"></span>
    <span class="partner partner--dark"></span>
    <span class="partner"></span>
    <span class="partner"></span>
    <span class="partner"></span>
    <span class="partner"></span>
    <span class="partner partner--pink"></span>
    <span class="partner partner--dark"></span>
  </div>

  <div class="town-photo" role="img" aria-label="Faded aerial view of the town in blue tones"></div>
  <svg class="back-swoosh" viewBox="0 0 763 175" aria-hidden="true">
    <defs>
      <linearGradient id="footBlue" x1="0" y1="0" x2="1" y2="0">
        <stop offset="0" stop-color="#1e56c0"/>
        <stop offset="1" stop-color="#0b2f86"/>
      </linearGradient>
    </defs>
    <path d="M0 118 C160 160 360 170 520 140 C620 120 700 80 763 58 V175 H0 Z" fill="url(#footBlue)"/>
    <path d="M0 118 C160 160 360 170 520 140 C620 120 700 80 763 58" fill="none" stroke="#fff" stroke-width="5"/>
  </svg>
  <p class="site">brightmererealty.com</p>
  <ul class="contacts">
    <li>Daniel Marlowe : daniel@brightmererealty.com</li>
    <li>Ruth Marlowe : ruth@brightmererealty.com</li>
  </ul>
</section>

</body>
</html>
```